Corvane Vitality - Health, Wellness, Fitness Consultants

Corvane Vitality are Corvane Vitality are leading consultants to the Health, Wellness and Fitness industry​​, with over 25 years experience working with some of the biggest global worldwide brands from equipment providers and facility operators to mass participation events and obstacle course races. Corvane Vitality is a multi disciplined business specialising in helping brands grow through insight, strategy creation and valuable sector collaboration, We are the official exclusive distributors of Brisk Frame bodyweight training products for the UK and Ireland, Official Partners of Obstacle Course Race and Adventure Racing Metro Clash & Dauntless Circuit - I would like a black background card, 1 side Corvane Vitality logo only other side Official, Exclusive, Distributors and Partners in the UK & Ireland. Then list Metro Clash, Brisk Frame, Dauntless Circuit contact details at very bottom Founder / Director - Rob Pelham
Mobile - +44(0)7461903257
E - Mail - rob.pelham@corvanevitality.example
Web - www.corvanevitality.example
Skype - corvanevitality

```html
<!DOCTYPE html>
<html lang="en">
<head>
<meta charset="utf-8">
<title>Corvane Vitality – Business Card</title>
<link href="https://fonts.googleapis.com/css2?family=Crimson+Text&family=Open+Sans:wght@400;600;800&family=Tenor+Sans&display=swap" rel="stylesheet">
<style>
  :root {
    --stage: #3b3b3b;
    --card: #1e1e1e;
    --lime: #b8c761;
    --gold: #c9a23c;
    --orange: #e8791b;
    --blue: #1d8fd8;
    --white: #f2f2f2;
    --ink: #1e1e1e;
  }
  * { box-sizing: border-box; margin: 0; padding: 0; }
  html, body { width: 799px; height: 1200px; overflow: hidden; }
  body { background: var(--stage); position: relative; }

  .card {
    position: absolute;
    left: 50px;
    width: 700px;
    height: 400px;
    background: var(--card);
    overflow: hidden;
    box-shadow: 0 12px 30px rgba(0,0,0,.45);
  }
  .card--front { top: 110px; }
  .card--back { top: 690px; }

  /* front */
  .front-mark {
    position: absolute; left: 0; right: 0; top: 130px;
    text-align: center;
    font-family: "Tenor Sans", sans-serif;
    font-size: 64px; color: var(--lime);
  }
  .front-tagline {
    position: absolute; left: 0; right: 0; top: 250px;
    text-align: center;
    font-family: "Crimson Text", serif;
    font-size: 26px; color: var(--gold); letter-spacing: .5px;
  }

  /* back */
  .brand { position: absolute; left: 40px; top: 34px; }
  .brand__name {
    font-family: "Tenor Sans", sans-serif;
    font-size: 42px; color: var(--lime); line-height: 1;
  }
  .brand__tagline {
    font-family: "Open Sans", sans-serif;
    font-size: 14px; color: var(--white); margin-top: 4px;
  }

  .partners {
    position: absolute; left: 40px; top: 168px;
    font-family: "Open Sans", sans-serif; font-weight: 800;
    display: flex; flex-direction: column; gap: 6px;
  }
  .partner { font-size: 26px; line-height: 1.1; display: flex; align-items: center; gap: 8px; }
  .partner--brisk { color: var(--blue); }
  .partner--metro { color: var(--white); }
  .partner--dauntless { color: var(--orange); font-size: 22px; }
  .partner__dot { width: 22px; height: 22px; border-radius: 50%; border: 2px solid var(--white); }

  .person { position: absolute; left: 420px; top: 150px; }
  .person__name {
    font-family: "Open Sans", sans-serif; font-weight: 800;
    font-size: 28px; color: var(--lime); text-transform: uppercase; line-height: 1;
  }
  .person__role {
    font-family: "Open Sans", sans-serif; font-size: 15px; color: var(--white); margin-top: 4px;
  }

  .contacts {
    position: absolute; left: 380px; top: 232px; list-style: none;
    font-family: "Open Sans", sans-serif; font-size: 15px; color: var(--white);
  }
  .contacts li { display: flex; align-items: center; gap: 10px; line-height: 24px; }
  .contacts svg { width: 14px; height: 14px; fill: var(--lime); flex: none; }

  .bands { position: absolute; left: 0; top: 0; width: 700px; height: 400px; }
  .skype {
    position: absolute; left: 360px; top: 350px;
    display: flex; align-items: center; gap: 10px;
    font-family: "Open Sans", sans-serif; font-size: 20px; color: var(--ink);
  }
  .skype__dot { width: 16px; height: 16px; border-radius: 50%; background: var(--ink); }
</style>
</head>
<body>

<section class="card card--front">
  <div class="front-mark">Corvane Vitality</div>
  <div class="front-tagline">Health | Wellness | Fitness | Consultants</div>
</section>

<section class="card card--back">
  <svg class="bands" viewBox="0 0 700 400" aria-hidden="true">
    <polygon points="0,368 320,368 306,400 0,400" fill="var(--orange)"/>
    <polygon points="296,400 330,330 700,330 700,400" fill="var(--lime)"/>
  </svg>

  <div class="brand">
    <div class="brand__name">Corvane Vitality</div>
    <div class="brand__tagline">Health, Wellness, Fitness, Consultants</div>
  </div>

  <div class="partners">
    <div class="partner partner--brisk">Brisk Frame</div>
    <div class="partner partner--metro">Metro Clash</div>
    <div class="partner partner--dauntless"><span class="partner__dot"></span>Dauntless Circuit</div>
  </div>

  <div class="person">
    <div class="person__name">Rob Pelham</div>
    <div class="person__role">Founder / Director</div>
  </div>

  <ul class="contacts">
    <li>
      <svg viewBox="0 0 16 16"><path d="M3 1h3l1 4-2 1c1 2 3 4 5 5l1-2 4 1v3c0 1-1 2-2 2C7 15 1 9 1 3c0-1 1-2 2-2z"/></svg>
      +44(0)7461903257
    </li>
    <li>
      <svg viewBox="0 0 16 16"><path d="M1 3h14v10H1z M2 4l6 5 6-5" fill="none" stroke="var(--lime)" stroke-width="1.6"/></svg>
      rob.pelham@corvanevitality.example
    </li>
    <li>
      <svg viewBox="0 0 16 16"><circle cx="8" cy="8" r="6.5" fill="none" stroke="var(--lime)" stroke-width="1.5"/><path d="M1.5 8h13M8 1.5c-3 3.5-3 9.5 0 13M8 1.5c3 3.5 3 9.5 0 13" fill="none" stroke="var(--lime)" stroke-width="1.2"/></svg>
      www.corvanevitality.example
    </li>
  </ul>

  <div class="skype"><span class="skype__dot"></span>corvanevitality</div>
</section>

</body>
</html>
```